Redesign of an educational Eye website for Medical Students and Healthcare professionals

www.corvellelearninghub.com is an educational resource, illustrated using high quality 3D animations, for undergraduate medical students and healthcare professionals to learn about the anatomy of the human eye and associated common eye disorders.

The website was originally developed (using a Joomla template) a couple of years ago and we now want to update the brand and design of the site. Example content and animations can be found at https://www.corvellelearninghub.com/overview or https://www.corvellelearninghub.com/ocular-anatomy/orbital-anatomy

We would like a new logo and home page design (to include new colour palette, fonts and updated overall design).

The attached PowerPoint contains an example layout of the revised components we want to appear on the new Home page. We plan to have a hero panel at the top of page playing a short video of some of the animations. Similar to how this site works (www.zeptal.uk.com).

We want the new site to feel Professional, Modern and Clean and simple.

Target Market(s)

Undergraduate medical students and Healthcare Professionals

Industry/Entity Type

Medical

Logo Text

Corvelle Learning Hub

Number of Pages Required

1 page

Font styles to use
Sans Serif

Colors

Designer to choose colors to be used in the design.

```html
<!DOCTYPE html>
<html lang="en">
<head>
<meta charset="utf-8">
<title>Corvelle Learning Hub</title>
<link rel="stylesheet" href="https://fonts.googleapis.com/css2?family=Roboto:wght@400;500;700&display=swap">
<style>
:root{
  --teal:#12b5b4;
  --teal-dark:#0ea3a2;
  --slate:#434b55;
  --ink:#2f3336;
  --muted:#8a8f94;
  --light:#f1f1f1;
  --white:#ffffff;
}
*{box-sizing:border-box;margin:0;padding:0}
html,body{width:1200px;height:3056px;overflow:hidden}
body{font-family:'Roboto',sans-serif;color:var(--ink);background:var(--white);position:relative}
section,header,footer{position:absolute;left:0;width:1200px}
.abs{position:absolute}

/* header */
.site-header{top:0;height:54px;background:var(--white);border-bottom:2px solid var(--teal)}
.brand{left:88px;top:10px;font-size:26px;font-weight:500;color:var(--teal);letter-spacing:.2px}
.main-nav a{position:absolute;top:20px;font-size:14px;font-weight:500;color:var(--ink);text-decoration:none;text-transform:uppercase}
.main-nav a.active{border-bottom:2px solid var(--teal);padding-bottom:6px}
.sign-in{right:0;top:0;width:206px;height:54px;background:var(--teal);color:var(--white);font-size:13px;display:flex;align-items:center;justify-content:center;gap:8px}

/* hero */
.hero{top:54px;height:542px;background:var(--white);text-align:center}
.hero-visual{left:240px;top:40px;width:760px;height:470px;border-radius:50%;background:radial-gradient(circle at 50% 50%,#f7e4dc 0%,#f8f1ee 45%,#ffffff 72%)}
.hero-kicker{left:0;width:100%;top:138px;font-size:40px;font-weight:700;color:var(--teal)}
.hero-title{left:0;width:100%;top:180px;font-size:62px;font-weight:700;color:var(--teal);letter-spacing:.5px}
.hero-copy{left:230px;width:740px;top:266px;font-size:14px;line-height:22px;font-weight:500;color:#222}
.btn{display:flex;align-items:center;justify-content:center;font-size:13px;font-weight:700;text-transform:uppercase;letter-spacing:.3px}
.btn-solid{left:267px;top:359px;width:279px;height:36px;background:var(--teal);color:var(--white)}
.btn-outline{left:564px;top:359px;width:369px;height:36px;border:2px solid var(--slate);color:var(--slate);background:var(--white)}

/* team */
.team{top:596px;height:320px;background:var(--slate)}
.section-title{left:0;width:100%;text-align:center;font-weight:500;text-transform:uppercase}
.team .section-title{top:42px;font-size:30px;color:var(--white)}
.member{top:100px;width:238px;height:168px;border:2px solid #d8dadc;background:var(--white)}
.member-photo{left:0;top:0;width:234px;height:112px;background:linear-gradient(180deg,#f2f3f4,#dcdfe2)}
.member-info{left:0;top:112px;width:234px;height:52px;background:var(--slate);color:var(--white);padding:6px 8px}
.member-info b{display:block;font-size:13px;font-weight:700}
.member-info span{font-size:12px;color:#dfe2e4}

/* why */
.why{top:916px;height:622px;background:var(--white)}
.why .section-title{top:44px;font-size:32px;color:var(--ink);letter-spacing:.5px}
.frame-line{border-color:var(--teal);border-style:solid}
.feature-img{background:linear-gradient(135deg,#1e4f86,#c56a32 60%,#e98d22)}
.feature-title{font-size:22px;font-weight:700;color:var(--teal)}
.feature-copy{font-size:13px;line-height:23px;color:var(--muted)}

/* trusted */
.trusted{top:1538px;height:268px;background:var(--light)}
.trusted .section-title{top:46px;font-size:30px;color:var(--ink)}
.partner-badge{left:108px;top:98px;width:114px;height:114px;background:#dcdcdc;border-radius:8px}
.partner-slot{top:126px;width:190px;text-align:center;font-size:32px;line-height:38px;color:#1a1a1a}

/* testimonials */
.testimonials{top:1806px;height:366px;background:var(--teal);color:var(--white)}
.testimonials .section-title{top:44px;font-size:29px;line-height:38px}
.quote-photo{left:210px;top:140px;width:118px;height:118px;border-radius:50%;background:linear-gradient(180deg,#e7ecef,#5b6d80);border:4px solid var(--white)}
.quote-mark{left:294px;top:140px;width:46px;height:46px;border-radius:50%;background:var(--white)}
.quote-name{left:190px;top:262px;font-size:15px;font-weight:700}
.quote-name span{font-weight:400;font-size:13px}
.quote-text{left:364px;top:162px;width:640px;font-size:14px;line-height:24px}
.dots{left:0;width:100%;top:306px;display:flex;justify-content:center;gap:8px}
.dots i{width:9px;height:9px;border-radius:50%;background:var(--white);opacity:.55}
.dots i.on{opacity:1}

/* trial */
.trial{top:2172px;height:214px;background:var(--slate);color:var(--white);text-align:center}
.trial .section-title{top:44px;font-size:29px;font-weight:700}
.trial-copy{left:0;width:100%;top:94px;font-size:14px}
.btn-trial{left:504px;top:122px;width:194px;height:38px;background:var(--teal);color:var(--white)}

/* charity */
.charity{top:2386px;height:226px;background:linear-gradient(90deg,#efe7dc,#f4efe8 55%,#ece6df)}
.charity-photo{left:100px;top:14px;width:260px;height:196px;border-radius:40%;background:radial-gradient(circle,#c9a487 0%,#a9a39c 45%,rgba(240,232,222,0) 72%)}
.charity-panel{left:442px;top:40px;width:758px;height:154px;background:rgba(255,255,255,.9);padding:24px 36px}
.charity-panel h3{font-size:29px;font-weight:400;color:var(--teal);text-transform:uppercase;margin-bottom:14px}
.charity-panel p{font-size:14px;line-height:24px;color:#444}

/* newsletter */
.newsletter{top:2612px;height:152px;background:var(--teal)}
.newsletter .section-title{top:34px;font-size:29px;font-weight:700;color:var(--white)}
.nl-input{left:320px;top:80px;width:446px;height:40px;background:var(--white);border:2px solid #d0eeee}
.nl-btn{left:772px;top:80px;width:146px;height:40px;background:var(--slate);color:var(--white);font-weight:500}

/* footer */
.site-footer{top:2764px;height:292px;background:var(--slate);color:var(--white)}
.foot-col h4{font-size:14px;font-weight:700;color:var(--teal);text-transform:uppercase;margin-bottom:12px}
.foot-col li{list-style:none;font-size:13px;line-height:26px}
.foot-col.res li{line-height:31px}
.foot-rule{left:0;top:186px;width:100%;height:1px;background:#5d656e}
.social{left:0;width:100%;top:204px;display:flex;justify-content:center;gap:14px}
.social i{width:34px;height:34px;border-radius:50%;background:#4c78c9}
.copyright{left:0;width:100%;top:258px;text-align:center;font-size:14px;color:#dfe2e4}
</style>
</head>
<body>

<header class="site-header">
  <div class="abs brand">Corvelle Learning Hub</div>
  <nav class="main-nav">
    <a href="#" class="active" style="left:438px">Home</a>
    <a href="#" style="left:548px">About</a>
    <a href="#" style="left:662px">Chapters</a>
    <a href="#" style="left:802px">FAQ</a>
    <a href="#" style="left:898px">Contact</a>
  </nav>
  <div class="abs sign-in">
    <svg width="14" height="14" viewBox="0 0 14 14" aria-hidden="true"><circle cx="7" cy="4" r="3.2" fill="#fff"/><path d="M1 14c0-4 2.6-6 6-6s6 2 6 6z" fill="#fff"/></svg>
    <span>|&nbsp; SIGN - IN</span>
  </div>
</header>

<section class="hero">
  <div class="abs hero-visual" role="img" aria-label="Faint labelled cross-section of the human eye"></div>
  <div class="abs hero-kicker">LEARN</div>
  <h1 class="abs hero-title">FASTER AND SMARTER</h1>
  <p class="abs hero-copy">Lorem ipsum dolor sit amet, consectetuer adipiscing elit, sed diam nonummy nibh euismod tincidunt ut laoreet &nbsp;Lorem ipsum dolor sit amet, consectetuer adipiscing elit, sed diam nonummy nibh euismod tincidunt ut laoreet</p>
  <a class="abs btn btn-solid">Undergraduates – Learn More</a>
  <a class="abs btn btn-outline">Healthcare Professionals &nbsp;– Learn More</a>
</section>

<section class="team">
  <h2 class="abs section-title">Meet the Team</h2>
  <div class="abs member" style="left:86px"><div class="abs member-photo" role="img" aria-label="Portrait of team member"></div><div class="abs member-info"><b>John Doe</b><span>consectetuer adipiscing elit,</span></div></div>
  <div class="abs member" style="left:350px"><div class="abs member-photo" role="img" aria-label="Portrait of team member"></div><div class="abs member-info"><b>Jane Doe</b><span>consectetuer adipiscing elit,</span></div></div>
  <div class="abs member" style="left:613px"><div class="abs member-photo" role="img" aria-label="Portrait of team member"></div><div class="abs member-info"><b>John Doe</b><span>consectetuer adipiscing elit,</span></div></div>
  <div class="abs member" style="left:876px"><div class="abs member-photo" role="img" aria-label="Portrait of team member"></div><div class="abs member-info"><b>John Doe</b><span>consectetuer adipiscing elit,</span></div></div>
</section>

<section class="why">
  <h2 class="abs section-title">Why Corvelle Learning Hub</h2>

  <div class="abs frame-line" style="left:84px;top:94px;width:52px;height:150px;border-width:2px 0 0 2px"></div>
  <div class="abs frame-line" style="left:398px;top:168px;width:104px;height:150px;border-width:0 2px 2px 0"></div>
  <div class="abs feature-img" style="left:92px;top:100px;width:403px;height:212px" role="img" aria-label="Diagram of the binocular visual field"></div>
  <h3 class="abs feature-title" style="left:526px;top:96px">Credible</h3>
  <p class="abs feature-copy" style="left:526px;top:130px;width:578px">Lorem Ipsum is simply dummy text of the printing and typesetting industry. Lorem Ipsum has been the industry's standard dummy text ever since the 1500s, when an unknown printer took a galley of type and scrambled it to make.<br>survived not only five centuries.</p>

  <h3 class="abs feature-title" style="left:500px;top:346px;width:176px;text-align:right">Visual</h3>
  <p class="abs feature-copy" style="left:96px;top:380px;width:580px;text-align:right">Lorem Ipsum is simply dummy text of the printing and typesetting industry. Lorem Ipsum has been the industry's standard dummy text ever since the 1500s, when an unknown printer took a galley of type and scrambled it to make.<br>survived not only five centuries.</p>
  <div class="abs frame-line" style="left:1052px;top:346px;width:62px;height:150px;border-width:2px 2px 0 0"></div>
  <div class="abs frame-line" style="left:700px;top:470px;width:110px;height:100px;border-width:0 0 2px 2px"></div>
  <div class="abs feature-img" style="left:707px;top:351px;width:403px;height:214px;background:linear-gradient(135deg,#e7c3a7,#b88b6e 50%,#1f4f8e)" role="img" aria-label="Illustration of the temporal and nasal field of view"></div>
</section>

<section class="trusted">
  <h2 class="abs section-title">Trusted Across the World</h2>
  <div class="abs partner-badge" role="img" aria-label="Partner badge"></div>
  <div class="abs partner-slot" style="left:355px">Image Goes<br>Here</div>
  <div class="abs partner-slot" style="left:645px">Image Goes<br>Here</div>
  <div class="abs partner-slot" style="left:934px">Image Goes<br>Here</div>
</section>

<section class="testimonials">
  <h2 class="abs section-title">What are people saying<br>about Corvelle Learning Hub</h2>
  <div class="abs quote-photo" role="img" aria-label="Portrait of reviewer"></div>
  <div class="abs quote-mark">
    <svg width="46" height="46" viewBox="0 0 46 46" aria-hidden="true"><path d="M12 28c0-7 3-11 8-13l1 2c-3 2-4 4-4 6h4v9h-9zM24 28c0-7 3-11 8-13l1 2c-3 2-4 4-4 6h4v9h-9z" fill="#2f3336"/></svg>
  </div>
  <div class="abs quote-name">John Doe <span>| dummy text</span></div>
  <p class="abs quote-text">Has been the industry's standard dummy text ever since the 1500s, when an unknown printer took a galley of type and scrambled it to make a type specimen book. It has survived not only five centuries, but also the leap into electronic typesetting, remaining essentially unchanged. It was popularised in the 1960s with the release of Lettrafix.</p>
  <div class="abs dots"><i class="on"></i><i></i><i></i></div>
</section>

<section class="trial">
  <h2 class="abs section-title">Want to try Corvelle Learning Hub for free</h2>
  <p class="abs trial-copy">Lorem Ipsum is simply dummy text of the printing and typesetting industry.</p>
  <a class="abs btn btn-trial">Start Free Trial</a>
</section>

<section class="charity">
  <div class="abs charity-photo" role="img" aria-label="Cupped hands holding coins"></div>
  <div class="abs charity-panel">
    <h3>We give 10% of our profit to charity</h3>
    <p>Has been the industry's standard dummy text ever since the 1500s, when an unknown printer took a galley of type and scrambled it to make a type specimen book. It has survived not only</p>
  </div>
</section>

<section class="newsletter">
  <h2 class="abs section-title">Subscribe to our Newsletter</h2>
  <div class="abs nl-input"></div>
  <a class="abs btn nl-btn">Subscribe</a>
</section>

<footer class="site-footer">
  <div class="abs foot-col" style="left:86px;top:28px"><h4>Products</h4><ul><li>Employee Engagement</li><li>Employee Effectiveness</li><li>Employee Experience</li><li>Plans &amp; Pricing</li></ul></div>
  <div class="abs foot-col" style="left:390px;top:28px"><h4>Company</h4><ul><li>Our Story</li><li>Customers</li><li>Careers</li><li>Blog</li></ul></div>
  <div class="abs foot-col res" style="left:630px;top:28px"><h4>Resources</h4><ul><li>Lorem Ipsum is simply dummy text</li><li>Lorem Ipsum is simply dummy text</li><li>Lorem Ipsum is simply dummy text</li><li>Lorem Ipsum is simply dummy &nbsp;of</li></ul></div>
  <div class="abs foot-col" style="left:1021px;top:28px"><h4>Contact Us</h4><ul><li>Email Sales</li><li>Email Support</li></ul></div>
  <div class="abs foot-rule"></div>
  <div class="abs social"><i></i><i style="background:#2f9fe0"></i><i style="background:#4c6cc9"></i></div>
  <div class="abs copyright">Copyright © 2018 &nbsp;|&nbsp; All Rights Reserved.</div>
</footer>

</body>
</html>
```